Mobile Money & Fintech Solutions needs a business card design and logo

I need the design of a business card and a logo for my consultant, based in Asuncion Paraguay. I am in the Digital World category, specializing in Mobile Money, Fintech Solutions & e-commerce. I would like the design to reflect trust and above all encompass the area of ​​specialty of the services that I offer. (Mobile Money, Fintech Solutions & e-commerce)

Target Market(s)

Financial entities, companies wishing to undertake a Fintech or e-commerce project

Contact Information for Business Card

Marela Quintobri
Senior Advisory Consultant
Cel +595983417258
Skype ID marelaquintobri
Linkedin: http://lnkshort.example/8wXpq4Tz

Logo Text

Fintech Solutions&E-commerce

Requirements
Must have
• I would like it to be a fusion of symbols, example of the @, the $, cellular (cell) that can encompass the areas.
Nice to have
• Must be related to the Fintech area and / or Mobile MOney and e-commerce. It is a new consultancy, so there are no previous logos

```html
<!DOCTYPE html>
<html lang="en">
<head>
<meta charset="utf-8">
<title>Veranta – Business Card</title>
<link rel="stylesheet" href="https://fonts.googleapis.com/css2?family=Ubuntu:wght@400;500&family=Bree+Serif&display=swap">
<style>
  :root {
    --backdrop: #cdced2;
    --brand-blue: #0067ad;
    --brand-navy: #0f3e7b;
    --brand-green: #00965a;
    --brand-orange: #e87a1a;
    --paper: #f9f9f9;
    --ink: #2a2a2a;
    --white: #ffffff;
  }
  * { box-sizing: border-box; margin: 0; padding: 0; }
  html, body {
    width: 1200px; height: 1011px; overflow: hidden;
    background: var(--backdrop);
    font-family: "Ubuntu", sans-serif;
  }
  .card {
    position: absolute;
    left: 337px;
    width: 525px; height: 318px;
    overflow: hidden;
  }
  /* Front */
  .card--front { top: 159px; background: var(--brand-blue); color: var(--white); }
  .front-mark {
    position: absolute; left: 0; right: 0; top: 110px;
    display: flex; align-items: center; justify-content: center; gap: 14px;
  }
  .front-mark__dot {
    width: 34px; height: 34px; border-radius: 50%;
    border: 6px solid var(--white);
  }
  .front-mark__name {
    font-size: 46px; font-weight: 500; letter-spacing: 1px; line-height: 1;
  }
  .services {
    position: absolute; left: 0; right: 0; top: 279px;
    font-size: 18px; font-weight: 400; list-style: none;
  }
  .services li { position: absolute; white-space: nowrap; }
  .services li:nth-child(1) { left: 21px; }
  .services li:nth-child(2) { left: 193px; }
  .services li:nth-child(3) { left: 390px; }

  /* Back */
  .card--back { top: 534px; background: var(--paper); }
  .brand {
    position: absolute; left: 26px; top: 40px;
    display: flex; align-items: center; gap: 14px;
  }
  .brand__dot {
    width: 62px; height: 62px; border-radius: 50%;
    border: 9px solid var(--brand-navy);
  }
  .brand__name {
    font-size: 42px; font-weight: 500; color: var(--brand-navy);
    letter-spacing: 1px; line-height: 1;
  }
  .person { position: absolute; left: 30px; top: 158px; }
  .person__name {
    font-family: "Bree Serif", serif;
    font-size: 25px; color: var(--brand-navy); line-height: 1.2;
  }
  .person__role { font-size: 12.5px; color: var(--ink); margin-top: 4px; }
  .accent-band {
    position: absolute; left: 0; right: 0; top: 232px; bottom: 0;
    background: linear-gradient(90deg,
      var(--brand-orange) 0%, var(--brand-green) 30%, var(--brand-blue) 60%, var(--brand-blue) 100%);
  }
  .contacts {
    position: absolute; right: 28px; top: 240px;
    list-style: none; color: var(--white); font-size: 12.5px;
    text-align: right;
  }
  .contacts li {
    display: flex; align-items: center; justify-content: flex-end;
    gap: 8px; height: 19px;
  }
  .contacts .icon {
    width: 12px; height: 12px; border-radius: 50%; background: var(--white);
    flex: none;
  }
  .contacts svg.icon { background: none; border-radius: 0; }
</style>
</head>
<body>
  <section class="card card--front">
    <div class="front-mark">
      <span class="front-mark__dot"></span>
      <span class="front-mark__name">VERANTA</span>
    </div>
    <ul class="services">
      <li>Mobile Money</li>
      <li>Fintech Solutions</li>
      <li>E-Commerce</li>
    </ul>
  </section>

  <section class="card card--back">
    <div class="brand">
      <span class="brand__dot"></span>
      <span class="brand__name">VERANTA</span>
    </div>

    <div class="person">
      <h1 class="person__name">Marela Quintobri</h1>
      <p class="person__role">Senior Advisory Consultant</p>
    </div>

    <div class="accent-band" role="img" aria-label="Decorative flowing bands in orange, green and blue across the lower card"></div>

    <ul class="contacts">
      <li>marelaquintobri <span class="icon"></span></li>
      <li>marela-quintobri <span class="icon"></span></li>
      <li>+595983417258
        <svg class="icon" viewBox="0 0 12 12" aria-hidden="true">
          <path fill="#fff" d="M1,4 C1,2 3,1.5 6,1.5 C9,1.5 11,2 11,4 L11,5 L8.5,5 L8.5,3.8 L3.5,3.8 L3.5,5 L1,5 Z"/>
          <path fill="#fff" d="M3,6 L9,6 L10.5,10.5 L1.5,10.5 Z"/>
        </svg>
      </li>
    </ul>
  </section>
</body>
</html>
```